Flyer Design Project

We need a flyer design for our lock company called 'Harwell Bolts'. It will be an A5 flyer delivered to local households advertising the benefits of upgrading their existing door locks to higher security , insurance approved ones.
We have the basic text/layout details and are looking forward to receiving your designs to help in the first stage of our new advertising programme.

Target Market(s)

This flyer is intended for general households.
I will be printing the final flyer as double sided, so it can be the same both sides or different each side depending on layout/content etc. any ideas suggestions will be much appreciated.

Industry/Entity Type

Advertising

Requirements
Must have
• HEADING- Something along the lines of 'Security Update', 'Security News' etc.

1) Basic facts- Every 37 seconds a home somewhere in Britain is burgled. In 70% of these burglaries the offenders gain entry through a door.

SUB HEADING- Who has the keys to your home?

TEXT- Over the years keys are lost, lent, borrowed, duplicated or not even handed over from previous owners and/or tennants.
Not only does this make your home more likely to be burgled it may also mean that your insurance policy will not cover you. As part of your insurance requirements you must have approved locks fitted, if they are not this can invalidate your policy.
Upgrading your homes security by upgrading and ensuring your locks are approved is a simple, cost-effective way to ensure not only your homes security but also your peace of mind.
For a free, no-obligation quotation from your local specialists call Harwell Bolts on 01632 960418.

None of this text is essential but, i feel, gets the message across well. If you have other ideas then please feel free to use your own ideas.

At the bottom of the page in small lettering will be;

'Harwell Bolts' is a trading name of Harwell Gates ltd. registered company no. 7316952. VAT #.642 1938 57. 14 Mill Row, Ashcombe.

Our company uses red normally for our name etc. This is by no means a must have but may help, It would also be beneficial to have some photos etc. to help with the text. Any questions please ask.

Nice to have
• I look forward to receiving your ideas and interpretations, i hope this will lead to working with you on our other future projects.
Yours sincerely
Colin Marbury.

```html
<!DOCTYPE html>
<html lang="en">
<head>
<meta charset="utf-8">
<title>Harwell Bolts – Security News Flyer</title>
<link href="https://fonts.googleapis.com/css2?family=Baskervville&family=Libre+Baskerville:wght@400;700&display=swap" rel="stylesheet">
<style>
  :root {
    --brand-red: #e41b23;
    --ink: #1a1a1a;
    --box-grey: #474747;
    --canvas: #ffffff;
    --sheet-a: #ddd3d2;
    --sheet-b: #cdb7b3;
    --sheet-c: #e2d9d6;
    --key-metal: #b9b9bb;
    --lock-photo: #e9e9e9;
    --fitter-photo: #8a6a55;
  }
  * { margin: 0; padding: 0; box-sizing: border-box; }
  html, body { width: 1200px; height: 881px; overflow: hidden; background: var(--canvas); }
  body {
    position: relative;
    font-family: "Baskervville", "Libre Baskerville", serif;
    font-variant-numeric: lining-nums;
    color: var(--ink);
  }

  .page {
    position: absolute; top: 37px; width: 566px; height: 792px; overflow: hidden;
    background: linear-gradient(160deg, var(--sheet-c) 0%, var(--sheet-a) 45%, var(--sheet-b) 75%, var(--sheet-a) 100%);
  }
  .page--front { left: 24px; }
  .page--back { left: 613px; }
  .page > * { position: absolute; white-space: nowrap; }

  .brand {
    font-family: "Libre Baskerville", serif; font-weight: 700;
    color: var(--brand-red); letter-spacing: 0.2em;
  }
  .page--front .brand { left: 0; width: 100%; top: 20px; text-align: center; font-size: 28px; }
  .page--back .brand { left: 57px; top: 38px; font-size: 30px; }

  .headline {
    left: 0; width: 100%; top: 60px; text-align: center;
    font-size: 80px; font-weight: 400; line-height: 1;
  }

  .facts { left: 0; width: 100%; top: 162px; text-align: center; font-size: 33px; line-height: 47px; list-style: none; }
  .facts li + li { margin-top: 11px; }
  .facts strong { font-family: "Libre Baskerville", serif; font-size: 34px; }
  .facts .unit { font-size: 28px; }

  .keys-box {
    left: 21px; top: 395px; width: 164px; height: 203px; background: var(--box-grey);
    color: #fff; font-family: "Libre Baskerville", serif; font-weight: 700;
    font-size: 23px; line-height: 39.5px; text-align: center; padding-top: 4px;
  }
  .keys-text { left: 200px; width: 336px; top: 426px; text-align: center; font-size: 24px; line-height: 34px; }

  .alert { left: 26px; top: 628px; color: var(--brand-red); font-size: 33px; line-height: 46px; }

  .art { display: block; }
  .art--keys-front { left: 368px; top: 604px; }
  .art--keys-back { left: 422px; top: 21px; }

  .footer { left: 0; width: 100%; text-align: center; font-size: 13px; line-height: 17px; }
  .page--front .footer { top: 758px; }
  .page--back .footer { top: 748px; }

  .lead { left: 0; width: 100%; top: 88px; font-size: 28px; line-height: 37px; text-align: center; }

  .photo { left: 30px; width: 176px; height: 174px; }
  .photo--lock { top: 233px; background: linear-gradient(135deg, #f4f4f4, var(--lock-photo) 60%, #d7d7d7); }
  .photo--fitter { top: 430px; background: linear-gradient(135deg, #c9c1b8 0%, var(--fitter-photo) 45%, #5b4538 100%); }

  .copy { left: 237px; width: 322px; font-size: 21.5px; line-height: 31px; }
  .copy--insurance { top: 229px; }
  .copy--upgrade { top: 396px; }

  .cta { left: 0; width: 100%; top: 624px; text-align: center; color: var(--brand-red); font-size: 29.5px; line-height: 41px; }
</style>
</head>
<body>

<section class="page page--front">
  <p class="brand">Harwell Bolts</p>
  <h1 class="headline">Security News</h1>
  <ul class="facts">
    <li>• Every <strong>37<span class="unit">seconds</span></strong> a home<br>somewhere in Britain is burgled.</li>
    <li>• In <strong>70%</strong> of these burglaries<br>the offenders gain entry through<br>a door.</li>
  </ul>
  <h2 class="keys-box">Who has<br>the<br>KEYS<br>to Your<br>Home?</h2>
  <p class="keys-text">Over the years keys are lost,<br>lent, borrowed, duplicated<br>or not even handed over<br>from previous owners<br>and/or tennants.</p>
  <p class="alert">Your Home may not<br>be secure right now!</p>
  <svg class="art art--keys-front" width="170" height="135" viewBox="0 0 170 135" role="img" aria-label="Photo of a pair of keys on a ring">
    <rect x="0" y="0" width="170" height="135" rx="20" fill="var(--key-metal)" opacity="0.55"/>
  </svg>
  <p class="footer">'Harwell Bolts' is a trading name of Harwell Gates ltd.<br>Registered company no. 7316952. VAT #.642 1938 57. 14 Mill Row, Ashcombe</p>
</section>

<section class="page page--back">
  <p class="brand">Harwell Bolts</p>
  <svg class="art art--keys-back" width="110" height="64" viewBox="0 0 110 64" role="img" aria-label="Photo of a pair of keys on a ring">
    <rect x="0" y="0" width="110" height="64" rx="14" fill="var(--key-metal)" opacity="0.55"/>
  </svg>
  <p class="lead">Not only does this make your home more<br>likely to be burgled it may also mean that<br>your insurance policy will not cover you.</p>
  <div class="photo photo--lock" role="img" aria-label="Photo of an insurance approved mortice sash lock with keys"></div>
  <p class="copy copy--insurance">As part of your insurance<br>requirements you must have<br>approved locks fitted, if they<br>are not this can invalidate<br>your policy.</p>
  <div class="photo photo--fitter" role="img" aria-label="Photo of a locksmith fitting a lock to a front door"></div>
  <p class="copy copy--upgrade">Upgrading your homes<br>security by upgrading and<br>ensuring your locks are<br>approved is a simple,<br>cost-effective way to ensure<br>not only your homes security<br>but also your peace of mind.</p>
  <p class="cta">For a free, no-obligation quotation<br>from your local specialists call Harwell<br>Bolts on 01632 960418.</p>
  <p class="footer">'Harwell Bolts' is a trading name of Harwell Gates ltd.<br>Registered company no. 7316952. VAT #.642 1938 57. 14 Mill Row, Ashcombe</p>
</section>

</body>
</html>
```